IT Company based on Biology Business Needs a PowerPoint Design

We need a powerpoint design for a new company called 'Tall FERN'. We develop the machine learning solutions especially focused on deep learning algorithms for biology industry. Our initial product is a vision detection on biological images to help doctors diagnose the symptoms. We would like to see designs that use the color green.

Industry/Entity Type

Biotechnology

Requirements
Nice to have
• Lots of slide templates with company logo's look and feel

```html
<!DOCTYPE html>
<html lang="en">
<head>
<meta charset="utf-8">
<title>Tall FERN – Presentation Templates</title>
<link href="https://fonts.googleapis.com/css2?family=Ropa+Sans&display=swap" rel="stylesheet">
<style>
  :root {
    --fern-green: #7dc242;
    --fern-green-dark: #5aa02c;
    --canvas-grey: #cccccc;
    --slide-white: #ffffff;
    --ink: #1e1e1e;
    --muted: #555555;
    --shadow: rgba(0, 0, 0, 0.45);
  }
  * { box-sizing: border-box; margin: 0; padding: 0; }
  html, body { width: 1200px; height: 1200px; overflow: hidden; }
  body {
    background: var(--canvas-grey);
    font-family: "Ropa Sans", "Arial Narrow", sans-serif;
    font-weight: 400;
    position: relative;
  }
  .slide {
    position: absolute;
    width: 542px;
    height: 406px;
    background: var(--slide-white);
    box-shadow: 6px 8px 10px var(--shadow);
    overflow: hidden;
  }
  .slide--cover    { left: 34px;  top: 134px; }
  .slide--contents { left: 605px; top: 134px; }
  .slide--article  { left: 34px;  top: 577px; }
  .slide--closing  { left: 605px; top: 577px; }

  .band {
    position: absolute;
    top: 0; left: 0; height: 100%;
    background: var(--fern-green);
  }
  .slide--cover .band   { width: 163px; }
  .slide--contents .band,
  .slide--article .band { width: 46px; }
  .slide--closing .band { width: 302px; }

  .brand {
    position: absolute;
    display: flex;
    align-items: center;
    gap: 5px;
    color: var(--fern-green);
    font-weight: 400;
    letter-spacing: -0.5px;
    white-space: nowrap;
  }
  .brand__dot { border-radius: 50%; background: var(--fern-green); }
  .brand--large { font-size: 28px; }
  .brand--large .brand__dot { width: 12px; height: 12px; }
  .brand--small { font-size: 12px; gap: 3px; }
  .brand--small .brand__dot { width: 6px; height: 6px; }
  .brand--medium { font-size: 20px; }
  .brand--medium .brand__dot { width: 9px; height: 9px; }

  .slide--cover .brand { right: 28px; top: 42px; }
  .slide--contents .brand { right: 30px; top: 374px; }
  .slide--article .brand { left: 454px; top: 376px; }
  .slide--closing .brand { left: 324px; top: 316px; }

  .title {
    position: absolute;
    color: var(--fern-green);
    text-transform: uppercase;
    font-weight: 400;
    letter-spacing: 0.5px;
  }
  .slide--cover .title { left: 205px; top: 198px; font-size: 35px; }
  .slide--contents .title,
  .slide--article .title { left: 70px; top: 30px; font-size: 22px; }

  .cover-subtitle {
    position: absolute;
    left: 201px; top: 258px;
    width: 310px;
    font-size: 17.5px;
    font-weight: 400;
    line-height: 18px;
    color: var(--ink);
  }

  .contents {
    position: absolute;
    left: 70px; top: 76px;
    width: 432px;
    list-style: none;
  }
  .contents__item {
    display: flex;
    align-items: baseline;
    height: 17.9px;
    font-size: 9.6px;
    color: var(--fern-green);
  }
  .contents__item--sub {
    font-size: 7.4px;
    color: var(--muted);
    padding-left: 27px;
  }
  .contents__label { white-space: nowrap; }
  .contents__leader {
    flex: 1;
    border-bottom: 1px dotted currentColor;
    margin: 0 4px 0 3px;
    transform: translateY(-2px);
  }
  .contents__page {
    width: 12px;
    margin-left: 27px;
    text-align: right;
    font-size: 9px;
    color: var(--muted);
  }

  .article-lead {
    position: absolute;
    left: 70px; top: 61px;
    font-size: 17px;
    font-weight: 400;
    color: var(--ink);
  }
  .article-columns {
    position: absolute;
    left: 68px; top: 89px;
    width: 441px; height: 274px;
    column-count: 2;
    column-gap: 13px;
    font-size: 7.7px;
    font-weight: 400;
    line-height: 12px;
    color: var(--ink);
    text-align: justify;
    overflow: hidden;
  }
  .article-columns p { margin-bottom: 12px; }

  .contact {
    position: absolute;
    left: 324px; top: 362px;
    list-style: none;
    font-size: 6.6px;
    color: var(--muted);
  }
  .contact__line {
    display: flex;
    align-items: center;
    gap: 5px;
    height: 9px;
  }
  .contact__icon { width: 7px; height: 7px; flex: none; }
</style>
</head>
<body>

<section class="slide slide--cover">
  <div class="band"></div>
  <div class="brand brand--large"><span class="brand__dot"></span>Tall FERN</div>
  <h1 class="title">Click to add title</h1>
  <p class="cover-subtitle">Lorem ipsum dolor sit amet, consectetur adipisicing elit, sed do eiusmod tempor</p>
</section>

<section class="slide slide--contents">
  <div class="band"></div>
  <h2 class="title">Click to add title</h2>
  <ol class="contents">
    <li class="contents__item"><span class="contents__label">Lorem Ipsum is simply dummy text</span><span class="contents__leader"></span><span class="contents__page">1</span></li>
    <li class="contents__item contents__item--sub"><span class="contents__label">a) Of the printing and typesetting industry. Lorem Ipsum has been the try's</span><span class="contents__leader"></span><span class="contents__page">2</span></li>
    <li class="contents__item contents__item--sub"><span class="contents__label">b) Standard dummy text ever since the 1500s, when an unknown printer</span><span class="contents__leader"></span><span class="contents__page">2</span></li>
    <li class="contents__item"><span class="contents__label">Lorem Ipsum is simply dummy text is the basic dummy text</span><span class="contents__leader"></span><span class="contents__page">3</span></li>
    <li class="contents__item contents__item--sub"><span class="contents__label">make a type specimen book. It has survived not only five centuries</span><span class="contents__leader"></span><span class="contents__page">4</span></li>
    <li class="contents__item contents__item--sub"><span class="contents__label">leap into electronic typesetting, remaining</span><span class="contents__leader"></span><span class="contents__page">5</span></li>
    <li class="contents__item contents__item--sub"><span class="contents__label">larised in the 1960s with the release of transfer sheets containing</span><span class="contents__leader"></span><span class="contents__page">6</span></li>
    <li class="contents__item"><span class="contents__label">Lorem Ipsum is simply dummy text</span><span class="contents__leader"></span><span class="contents__page">7</span></li>
    <li class="contents__item"><span class="contents__label">Lorem Ipsum is simply dummy textlorem ipsum is</span><span class="contents__leader"></span><span class="contents__page">7</span></li>
  </ol>
  <div class="brand brand--small"><span class="brand__dot"></span>Tall FERN</div>
</section>

<section class="slide slide--article">
  <div class="band"></div>
  <h2 class="title">Click to add title</h2>
  <p class="article-lead">Lorem ipsum dolor sit amet, consectetur adipisicing elit, sed</p>
  <div class="article-columns">
    <p>Lorem Ipsum is simply dummy text of the printing and typesetting industry. Lorem Ipsum has been the industry's standard dummy text ever since the 1500s, when an unknown printer took a galley of type and scrambled it to make a type specimen book. It has survived not only five centuries, but also the leap into electronic typesetting, remaining essentially unchanged. It was popularised in the 1960s with the release of transfer sheets containing Lorem Ipsum passages, and more recently with desktop publishing software like a page layout program including versions of Lorem Ipsum.</p>
    <p>It is a long established fact that a reader will be distracted by the readable content of a page when looking at its layout. The point of using Lorem Ipsum is that it has a more-or-less normal distribution of letters, as opposed to using 'Content here, content here', making it look like readable English. Many desktop publishing packages and web page editors now use Lorem Ipsum as their default model text, and a search for 'lorem ipsum' will uncover many web sites still in their infancy. Vari</p>
    <p>Contrary to popular belief, Lorem Ipsum is not simply random text. It has roots in a piece of classical Latin literature from 45 BC, making it over 2000 years old. Oren Valdis, a Latin professor at Marrow Hill College in Eastvale, looked up one of the more obscure Latin words, consectetur, from a Lorem Ipsum passage, and going through the cites of the word in classical literature, discovered the undoubtable source. Lorem Ipsum comes from sections 1.10.32 and 1.10.33 of "de Rebus Verdantibus" (On Green Things) by Aurelian Tosk, written in 45 BC. This book is a treatise on the theory of ethics, very popular during the Renaissance. The first line of Lorem Ipsum, "Lorem ipsum dolor sit amet..", comes from a line in section 1.10.32.</p>
    <p>The standard chunk of Lorem Ipsum used since the 1500s is reproduced below for those interested. Sections 1.10.32 and 1.10.33 from "de Rebus Verdantibus" by Aurelian Tosk are also reproduced in their exact original form, accompanied by English versions from the 1914 translation by P. Wendle.</p>
    <p>There are many variations of passages of Lorem Ipsum available, but the majority have suffered alteration in some form, by injected humour, or randomised words which don't look even slightly believable. If you are going to use a passage of</p>
  </div>
  <div class="brand brand--small"><span class="brand__dot"></span>Tall FERN</div>
</section>

<section class="slide slide--closing">
  <div class="band"></div>
  <div class="brand brand--medium"><span class="brand__dot"></span>Tall FERN</div>
  <ul class="contact">
    <li class="contact__line">
      <svg class="contact__icon" viewBox="0 0 10 10" aria-hidden="true"><circle cx="5" cy="5" r="5" fill="#5aa02c"/><path d="M3 3.2c.3 1.8 1.6 3.3 3.6 3.8l.6-.9-1.1-.6-.5.5c-.7-.3-1.2-.9-1.5-1.6l.5-.5-.6-1.1z" fill="#fff"/></svg>
      +0 555.204.1187
    </li>
    <li class="contact__line">
      <svg class="contact__icon" viewBox="0 0 10 10" aria-hidden="true"><circle cx="5" cy="5" r="5" fill="#5aa02c"/><rect x="2.6" y="3.3" width="4.8" height="3.4" fill="none" stroke="#fff" stroke-width=".8"/><path d="M2.6 3.3 5 5.2l2.4-1.9" fill="none" stroke="#fff" stroke-width=".8"/></svg>
      hello@tallfern.example
    </li>
    <li class="contact__line">
      <svg class="contact__icon" viewBox="0 0 10 10" aria-hidden="true"><circle cx="5" cy="5" r="5" fill="#5aa02c"/><circle cx="5" cy="5" r="2.6" fill="none" stroke="#fff" stroke-width=".8"/><path d="M2.4 5h5.2M5 2.4v5.2" stroke="#fff" stroke-width=".6"/></svg>
      www.tallfern.example
    </li>
  </ul>
</section>

</body>
</html>
```